International oil and gas consultancy needs a business card design

We need a business card design for a new oil and gas consultancy business based in Perth Australia. This is a professional services business and needs a moderately conservative type of business card. The business card also needs to be simple and uncluttered. The colour of the business logo is dark red (see attached file).
The front of the card should have a white background and mainly black lettering and perhaps some use of dark red and/or grey (your choice).
The back of the card should have a light grey background with dark red, black and or both dark red & black lettering (your choice).
Please find attached a clear brief of how I would like the business card designed.

Hello Everyone, I have slightly modified the brief. The main change is to incorporate some dark red and grey colours into the card, while still keeping the black lettering dominant. I have made the changes in the attached detailed brief document. Regards

Please note, the front of the card must say Pelwick Review Services (in addition to the logo).

Conservative

• brief has been updated. please refer to attachment for details.

Front of the card MUST say Pelwick Review Services (in addition to the logo)

```html
<!DOCTYPE html>
<html lang="en">
<head>
<meta charset="utf-8">
<title>Pelwick Review Services – Business Card</title>
<link rel="stylesheet" href="https://fonts.googleapis.com/css2?family=Arimo:wght@400;700&display=swap">
<style>
  :root {
    --canvas-bg: #e4e5e8;
    --card-white: #ffffff;
    --card-grey: #e9e9eb;
    --brand-red: #9a1d22;
    --ink: #111111;
    --ink-soft: #333333;
    --faint-grey: #ececee;
    --faint-grey-back: #dcdcdf;
  }
  * { box-sizing: border-box; margin: 0; padding: 0; }
  html, body { width: 1200px; height: 600px; overflow: hidden; }
  body {
    background: var(--canvas-bg);
    font-family: "Arimo", Arial, sans-serif;
    color: var(--ink);
  }
  .canvas {
    position: relative;
    width: 1200px;
    height: 600px;
  }
  .card {
    position: absolute;
    top: 150px;
    width: 525px;
    height: 300px;
    overflow: hidden;
    box-shadow: 0 4px 14px rgba(0,0,0,0.25);
  }
  .card--front { left: 50px; background: var(--card-white); }
  .card--back { left: 625px; background: var(--card-grey); }

  .decor-area {
    position: absolute;
    left: 30px;
    top: 120px;
    width: 170px;
    height: 180px;
  }
  .card--front .decor-area {
    background: linear-gradient(180deg, rgba(236,236,238,0) 0%, var(--faint-grey) 55%);
  }
  .card--back .decor-area {
    left: 20px;
    top: 0;
    height: 300px;
    background: linear-gradient(180deg, var(--faint-grey-back) 0%, rgba(220,220,223,0.3) 100%);
  }

  .brand-mark {
    position: absolute;
    left: 30px;
    top: 58px;
    display: flex;
    align-items: center;
    gap: 12px;
  }
  .brand-mark__square {
    width: 34px;
    height: 34px;
    background: var(--brand-red);
  }
  .brand-mark__name {
    font-size: 21px;
    font-weight: 700;
    color: var(--brand-red);
    letter-spacing: 0.2px;
  }

  .contact-person {
    position: absolute;
    right: 34px;
    top: 128px;
    text-align: right;
  }
  .contact-person__name { font-size: 17px; font-weight: 700; line-height: 1.2; }
  .contact-person__role,
  .contact-person__region { font-size: 12.5px; line-height: 1.45; color: var(--ink-soft); }

  .contact-details {
    position: absolute;
    right: 34px;
    top: 206px;
    text-align: right;
    font-size: 12.5px;
    line-height: 1.5;
    color: var(--ink-soft);
  }

  .back-heading {
    position: absolute;
    left: 0;
    right: 0;
    top: 92px;
    text-align: center;
    font-size: 21px;
    font-weight: 700;
    letter-spacing: 0.3px;
    color: var(--brand-red);
  }
  .back-tagline {
    position: absolute;
    left: 0;
    right: 0;
    top: 135px;
    text-align: center;
    font-size: 16px;
    line-height: 1.3;
    color: var(--ink);
  }
  .service-list {
    position: absolute;
    left: 28px;
    right: 20px;
    bottom: 24px;
    display: flex;
    justify-content: space-between;
    list-style: none;
    font-size: 13px;
    color: var(--ink);
  }
  .service-list__item { display: flex; align-items: center; gap: 7px; }
  .service-list__dot { width: 7px; height: 7px; border-radius: 50%; background: var(--brand-red); }
</style>
</head>
<body>
<main class="canvas">
  <section class="card card--front" aria-label="Business card front">
    <div class="decor-area" role="img" aria-label="Faint grey oil rig decoration"></div>
    <div class="brand-mark">
      <span class="brand-mark__square"></span>
      <span class="brand-mark__name">Pelwick Review Services</span>
    </div>
    <div class="contact-person">
      <p class="contact-person__name">Dean Harrow</p>
      <p class="contact-person__role">Director</p>
      <p class="contact-person__region">Australasia and South East Asia</p>
    </div>
    <div class="contact-details">
      <p>+61 (0)408 316 592</p>
      <p>dean@pelwickreview.com</p>
      <p>www.pelwickreview.com</p>
    </div>
  </section>

  <section class="card card--back" aria-label="Business card back">
    <div class="decor-area" role="img" aria-label="Faint grey oil rig decoration"></div>
    <h1 class="back-heading">PELWICK REVIEW SERVICES</h1>
    <p class="back-tagline">Specialist Financial Consultants<br>to the Oil and Gas Industry</p>
    <ul class="service-list">
      <li class="service-list__item"><span class="service-list__dot"></span>Joint Venture Audits</li>
      <li class="service-list__item"><span class="service-list__dot"></span>Contract Audits</li>
      <li class="service-list__item"><span class="service-list__dot"></span>Operational Audits</li>
    </ul>
  </section>
</main>
</body>
</html>
```